High profile consulting company needs a Business Card Design

I need a business card design for a coaching /consulting company. We specialize in changing behaviors. Our services include therapy, workshops, life coaching, etc.

Check out our website to get a feel for our personality. www.tidewaterguidance.com

The new logo will be attached to the website soon, I have attached the new logo for your use on the business card.
Updates

I forgot to provide you with the company email under the "must have" section for the business card.  The website is:

 www.tidewaterguidance.com

I understand there's some trouble with the logo I uploaded.  I will try that again.  Thank you for your efforts.

Lauren

Thank you for some of your questions.  I prefer a one sided business card, and tend to like the white backgrounds.

I also made 2 small changes to the content.  

add MFT after the name:  Lauren Pettigrew, MFT

and the tag line needed more clarity once I saw it.  Please change it to:  Helping people grow through honest conversation and lasting everyday habits.

Thank you,
Lauren

Industry/Entity Type

Business

Requirements
Must have
• logo
Phone number: 321-555-0164
email: Lauren@tidewaterguidance.com
Lauren Pettigrew, MFT
President
Nice to have
• Helping people grow through honest conversation and lasting everyday habits.

```html
<!DOCTYPE html>
<html lang="en">
<head>
<meta charset="utf-8">
<title>Tidewater Guidance — Business Card Options</title>
<link href="https://fonts.googleapis.com/css2?family=Open+Sans:wght@400;600;700;800&family=Roboto+Condensed:wght@700&display=swap" rel="stylesheet">
<style>
  :root {
    --bg: #eceae6;
    --card: #ffffff;
    --green: #11704f;
    --grey: #87878a;
    --ink: #2f2f31;
    --rule: #c9c9c9;
    --label: #555555;
  }
  * { box-sizing: border-box; margin: 0; padding: 0; }
  html, body { width: 1200px; height: 782px; overflow: hidden; }
  body {
    position: relative;
    background: var(--bg);
    font-family: "Open Sans", Arial, sans-serif;
    color: var(--ink);
  }
  .option-label {
    position: absolute;
    top: 26px;
    width: 548px;
    text-align: center;
    font-size: 32px;
    font-weight: 700;
    color: var(--label);
  }
  .card {
    position: absolute;
    width: 548px;
    height: 312px;
    background: var(--card);
    border-radius: 24px;
    box-shadow: 0 4px 10px rgba(0,0,0,.18);
  }
  .card--front { top: 86px; }
  .card--back { top: 437px; }
  .col-1 { left: 47px; }
  .col-2 { left: 624px; }

  .brand { position: absolute; left: 52px; top: 52px; display: flex; align-items: center; }
  .brand-mark { width: 114px; height: 114px; flex: none; }
  .brand-name {
    margin-left: 16px;
    font-weight: 800;
    font-size: 38px;
    line-height: 1.02;
    letter-spacing: 1px;
    color: var(--green);
  }
  .tagline {
    position: absolute;
    left: 180px;
    top: 158px;
    font-family: "Roboto Condensed", "Arial Narrow", sans-serif;
    font-weight: 700;
    font-size: 8px;
    letter-spacing: .1px;
    text-transform: uppercase;
    color: var(--ink);
    white-space: nowrap;
  }
  .person {
    position: absolute;
    top: 210px;
    left: 0; right: 0;
    text-align: center;
    font-size: 18px;
    font-weight: 600;
  }
  .person-title {
    font-size: 13px;
    font-weight: 400;
    letter-spacing: .5px;
    margin-left: 4px;
    padding-left: 6px;
    border-left: 1px solid var(--ink);
  }
  .divider {
    position: absolute;
    top: 240px;
    left: 14px; right: 14px;
    height: 1px;
    background: var(--rule);
  }
  .contact {
    position: absolute;
    left: 0; right: 0;
    font-size: 13.5px;
    display: flex;
    justify-content: center;
    align-items: center;
    gap: 6px;
    white-space: nowrap;
  }
  .contact--primary { top: 248px; }
  .contact--web { top: 268px; }
  .icon { width: 12px; height: 12px; flex: none; }
  .at { color: var(--green); font-weight: 700; margin-left: 4px; }

  .back-brand {
    position: absolute;
    inset: 0;
    display: flex;
    flex-direction: column;
    align-items: center;
    justify-content: center;
    gap: 14px;
  }
  .back-mark { width: 170px; height: 170px; }
  .back-name {
    font-weight: 800;
    font-size: 24px;
    letter-spacing: 1px;
    color: var(--green);
  }
</style>
</head>
<body>

  <div class="option-label" style="left:47px">Option 1</div>
  <div class="option-label" style="left:624px">Option 2</div>

  <section class="card card--front col-1">
    <div class="brand">
      <svg class="brand-mark" viewBox="0 0 114 114"><circle cx="57" cy="57" r="53" fill="var(--grey)" stroke="var(--green)" stroke-width="7"/></svg>
      <div class="brand-name">TIDEWATER<br>GUIDANCE</div>
    </div>
    <p class="tagline">Helping people grow through honest conversation and lasting everyday habits</p>
    <p class="person">Lauren Pettigrew, MFT <span class="person-title">PRESIDENT</span></p>
    <div class="divider"></div>
    <p class="contact contact--primary">
      <svg class="icon" viewBox="0 0 12 12"><path d="M3 1 L5 3.5 L4 5 Q5.5 7.5 7 8 L8.5 7 L11 9 L9.5 11 Q3 10 1 2.5 Z" fill="var(--green)"/></svg>
      321-555-0164 <span class="at">@</span> Lauren@tidewaterguidance.com
    </p>
    <p class="contact contact--web">
      <svg class="icon" viewBox="0 0 12 12"><circle cx="6" cy="6" r="5.5" fill="var(--green)"/><path d="M0.5 6 H11.5 M6 0.5 V11.5" stroke="#fff" stroke-width=".8"/></svg>
      www.tidewaterguidance.com
    </p>
  </section>

  <section class="card card--front col-2">
    <div class="brand">
      <svg class="brand-mark" viewBox="0 0 114 114"><circle cx="57" cy="57" r="53" fill="var(--grey)" stroke="var(--green)" stroke-width="7"/></svg>
      <div class="brand-name">TIDEWATER<br>GUIDANCE</div>
    </div>
    <p class="tagline">Helping people grow through honest conversation and lasting everyday habits</p>
    <p class="person">Lauren Pettigrew, MFT <span class="person-title">PRESIDENT</span></p>
    <div class="divider"></div>
    <p class="contact contact--primary">
      <svg class="icon" viewBox="0 0 12 12"><path d="M3 1 L5 3.5 L4 5 Q5.5 7.5 7 8 L8.5 7 L11 9 L9.5 11 Q3 10 1 2.5 Z" fill="var(--green)"/></svg>
      321-555-0164 <span class="at">@</span> Lauren@tidewaterguidance.com
    </p>
    <p class="contact contact--web">
      <svg class="icon" viewBox="0 0 12 12"><circle cx="6" cy="6" r="5.5" fill="var(--green)"/><path d="M0.5 6 H11.5 M6 0.5 V11.5" stroke="#fff" stroke-width=".8"/></svg>
      www.tidewaterguidance.com
    </p>
  </section>

  <section class="card card--back col-1">
    <div class="back-brand">
      <svg class="back-mark" viewBox="0 0 170 170"><circle cx="85" cy="85" r="80" fill="var(--grey)" stroke="var(--green)" stroke-width="9"/></svg>
      <div class="back-name">TIDEWATER GUIDANCE</div>
    </div>
  </section>

  <section class="card card--back col-2">
    <div class="back-brand">
      <svg class="back-mark" viewBox="0 0 170 170"><circle cx="85" cy="85" r="80" fill="var(--green)"/></svg>
      <div class="back-name">TIDEWATER GUIDANCE</div>
    </div>
  </section>

</body>
</html>
```